Waterproofing Adhesive company needs design for bucket

We need a design for our 20kg/15kg and 4 kg bucket, Our companys name is Vorlent Co LLC based in Umm Al Quwain, United Arab Emirates . Our main business is into waterproofing paint and Adhesive manufacturing. We are looking for a creative design for our buckets and paper bags. The design have to be attractive, The color theme of our company is light orange and yellow. I have attached the company logo along with this.

Target Market(s)

B2b , construction companys
Maintenance company

Industry/Entity Type

Manufacturer

Requirements
Must have
• It must have the company logo
• a spcae in centre to write the different products names
Nice to have
• A attractive design for placing the bucket in retail shops

```html
<!DOCTYPE html>
<html lang="en">
<head>
<meta charset="utf-8">
<title>Vorlent Co LLC — Bucket Label</title>
<link href="https://fonts.googleapis.com/css2?family=Montserrat:wght@500;700&family=Roboto+Condensed:wght@400;700&display=swap" rel="stylesheet">
<style>
  :root {
    --canvas: #ffffff;
    --panel-light: #f5f5f5;
    --panel-grey: #d6d6d6;
    --steel: #8f8f8f;
    --brand-orange: #e2601a;
    --deep-orange: #cf4a16;
    --burnt-orange: #c9420f;
    --sun-yellow: #f4cf3a;
    --pale-yellow: #f8e27a;
    --warm-yellow: #f0b52c;
    --amber: #eb9a22;
    --cream: #fbf1dc;
    --ink-red: #7a1d12;
    --ink-dark: #5a2a18;
  }
  * { box-sizing: border-box; margin: 0; padding: 0; }
  html, body { width: 1200px; height: 960px; overflow: hidden; background: var(--canvas); }
  .canvas { position: relative; width: 1200px; height: 960px; }

  .label {
    position: absolute; left: 20px; top: 220px; width: 1160px; height: 520px;
    background: linear-gradient(90deg, var(--panel-light), var(--panel-grey) 60%, var(--panel-light));
    overflow: hidden;
  }
  .brand-stripe { position: absolute; left: 0; top: 0; width: 26px; height: 100%; background: var(--brand-orange); }
  .brand-stripe-grey { position: absolute; left: 36px; top: 0; width: 8px; height: 100%; background: var(--steel); }
  .brand-stripe-orange { position: absolute; left: 70px; top: 0; width: 40px; height: 62%; background: linear-gradient(180deg, var(--deep-orange), var(--brand-orange)); }

  .artwork-field {
    position: absolute; left: 170px; top: 22px; right: 0; bottom: 22px;
    border-radius: 28px 0 0 150px;
    border-top: 6px solid var(--cream);
    border-left: 6px solid var(--cream);
    overflow: hidden;
    background:
      radial-gradient(ellipse 140px 34px at 380px 200px, rgba(201,66,15,.75), rgba(201,66,15,0) 100%),
      radial-gradient(ellipse 200px 40px at 560px 185px, rgba(201,66,15,.7), rgba(201,66,15,0) 100%),
      radial-gradient(ellipse 380px 80px at 460px 205px, rgba(226,96,26,.8), rgba(226,96,26,0) 100%),
      radial-gradient(ellipse 300px 60px at 860px 215px, rgba(226,96,26,.65), rgba(226,96,26,0) 100%),
      radial-gradient(ellipse 160px 40px at 160px 240px, rgba(235,154,34,.8), rgba(235,154,34,0) 100%),
      radial-gradient(ellipse 220px 90px at 250px 360px, rgba(248,226,122,.9), rgba(248,226,122,0) 100%),
      radial-gradient(ellipse 180px 70px at 520px 390px, rgba(235,154,34,.55), rgba(235,154,34,0) 100%),
      radial-gradient(ellipse 240px 80px at 720px 340px, rgba(248,226,122,.7), rgba(248,226,122,0) 100%),
      radial-gradient(ellipse 200px 70px at 120px 60px, rgba(248,226,122,.85), rgba(248,226,122,0) 100%),
      radial-gradient(ellipse 260px 70px at 640px 60px, rgba(235,154,34,.45), rgba(235,154,34,0) 100%),
      radial-gradient(ellipse 160px 60px at 380px 440px, rgba(240,181,44,.8), rgba(240,181,44,0) 100%),
      linear-gradient(165deg, var(--sun-yellow) 0%, var(--warm-yellow) 40%, #f3c542 68%, var(--sun-yellow) 100%);
  }
  .artwork-field::after {
    content: ""; position: absolute; inset: 0;
    background:
      repeating-linear-gradient(172deg, rgba(255,255,255,.06) 0 6px, rgba(255,255,255,0) 6px 18px),
      repeating-linear-gradient(8deg, rgba(207,74,22,.05) 0 4px, rgba(207,74,22,0) 4px 22px);
  }

  .brand-mark { position: absolute; left: 58px; bottom: 40px; width: 100px; text-align: center; }
  .brand-dot { width: 56px; height: 56px; border-radius: 50%; background: var(--brand-orange); margin: 0 auto 10px; }
  .brand-name { font: 700 15px/1.15 "Roboto Condensed", sans-serif; color: var(--brand-orange); }

  .product-frame {
    position: absolute; left: 300px; top: 150px; width: 470px; height: 200px;
    border: 4px solid var(--cream); padding: 12px;
  }
  .product-frame-inner {
    width: 100%; height: 100%; border: 2px solid var(--cream);
    display: flex; flex-direction: column; align-items: center; justify-content: center; gap: 10px;
    color: var(--cream); font-family: "Montserrat", sans-serif; text-align: center;
  }
  .product-tier { font-weight: 500; font-size: 15px; letter-spacing: 3px; }
  .product-name { font-weight: 700; font-size: 44px; letter-spacing: 2px; line-height: 1; }
  .product-type { font-weight: 500; font-size: 14px; letter-spacing: 2px; }

  .info-panel {
    position: absolute; top: 70px; width: 175px; height: 390px;
    background: rgba(251,241,220,.55); border: 3px solid var(--cream);
    padding: 12px 10px; font: 400 9.5px/1.45 "Roboto Condensed", sans-serif; color: var(--ink-dark);
    overflow: hidden;
  }
  .info-panel.hazard { left: 790px; }
  .info-panel.details { left: 975px; background: rgba(251,241,220,.85); }
  .hazard-title { font-weight: 700; font-size: 12px; color: var(--ink-red); margin-bottom: 6px; }
  .hazard-list { list-style: none; }
  .hazard-list li { margin-bottom: 3px; }
  .hazard-list .strong { font-weight: 700; color: var(--ink-red); }
</style>
</head>
<body>
<div class="canvas">
  <section class="label">
    <div class="brand-stripe"></div>
    <div class="brand-stripe-grey"></div>
    <div class="brand-stripe-orange"></div>

    <div class="artwork-field" role="img" aria-label="Watercolour wash in yellow and orange with a burnt orange streak across the middle of the label"></div>

    <div class="brand-mark">
      <div class="brand-dot"></div>
      <div class="brand-name">Vorlent Co LLC</div>
    </div>

    <div class="product-frame">
      <div class="product-frame-inner">
        <div class="product-tier">• PREMIUM •</div>
        <div class="product-name">PRODUCT NAME</div>
        <div class="product-type">• INDUSTRIAL PAINT •</div>
      </div>
    </div>

    <div class="info-panel hazard">
      <div class="hazard-title">DANGER</div>
      <ul class="hazard-list">
        <li>Flammable liquid and vapour.</li>
        <li>May be fatal if swallowed and enters airways.</li>
        <li>Causes serious eye irritation.</li>
        <li>Harmful to aquatic life with long lasting effects.</li>
        <li>Keep away from heat/sparks/open flames/hot surfaces.</li>
        <li>Keep container tightly closed.</li>
        <li>Wash hands thoroughly after handling.</li>
        <li>Wear protective gloves/protective clothing/eye protection/face protection.</li>
        <li>IF INHALED: Remove person to fresh air and keep at rest in a position comfortable for breathing.</li>
        <li class="strong">Call a POISON CENTER or doctor/physician if you feel unwell.</li>
        <li class="strong">Contains: 2-METHOXY-1-METHYLETHYLACETATE</li>
      </ul>
    </div>

    <div class="info-panel details">
      <p>Lorem ipsum dolor sit amet, consectetur adipisicing elit, sed do eiusmod tempor incididunt ut labore et dolore magna aliqua. Ut enim ad minim veniam, quis nostrud exercitation ullamco laboris nisi ut aliquip ex ea commodo consequat. Duis aute irure dolor in reprehenderit in voluptate velit esse cillum dolore eu fugiat nulla pariatur. Excepteur sint occaecat cupidatat non proident, sunt in culpa qui officia deserunt mollit anim id est laborum. Sed ut perspiciatis unde omnis iste natus error sit voluptatem accusantium doloremque laudantium, totam rem aperiam, eaque ipsa quae ab illo inventore veritatis et quasi architecto beatae vitae dicta sunt explicabo. Nemo enim ipsam voluptatem quia voluptas sit aspernatur aut odit aut fugit, sed quia consequuntur magni dolores eos qui ratione voluptatem sequi nesciunt. Neque porro quisquam est, qui dolorem ipsum quia dolor sit amet.</p>
    </div>
  </section>
</div>
</body>
</html>
```